Business Card Design Project

My business sells promotional merchandise to large blue chip companies. Gear like polo shirts, drink bottles, pens, basically anything that you can put a company logo onto.

I need the following elements included:
Logo as attached
Peter Hallorand Managing Director
21 Kestrel Court Thornlea 4168
mobile 0438 612054
email tidewell@tidewellcoastal.com.au

Promotional Merchandise with a difference

Mature age Marketing Managers

Business

```html
<!DOCTYPE html>
<html lang="en">
<head>
<meta charset="utf-8">
<title>Tidewell Business Card</title>
<link rel="stylesheet" href="https://fonts.googleapis.com/css2?family=Jost:wght@400;500&display=swap">
<style>
  :root {
    --navy: #172266;
    --paper: #ffffff;
    --silver: #e6e8ee;
    --bg-top: #d8d9da;
    --bg-bottom: #f6f6f6;
  }
  * { margin: 0; padding: 0; box-sizing: border-box; }
  html, body {
    width: 1043px;
    height: 1200px;
    overflow: hidden;
  }
  body {
    position: relative;
    background: linear-gradient(to bottom, var(--bg-top), var(--bg-bottom));
    font-family: "Jost", "Futura", sans-serif;
    color: var(--navy);
  }
  .card {
    position: absolute;
    left: 99px;
    width: 845px;
    height: 467px;
  }
  .card-front {
    top: 109px;
    background: var(--paper);
  }
  .card-back {
    top: 624px;
    background: var(--navy);
    display: flex;
    align-items: center;
    justify-content: center;
  }
  .brand-band {
    position: absolute;
    left: 0;
    top: 52px;
    width: 390px;
    height: 68px;
    background: var(--navy);
    display: flex;
    align-items: center;
    justify-content: flex-end;
    padding-right: 26px;
  }
  .brand-name {
    font-weight: 400;
    color: var(--silver);
    letter-spacing: 0.08em;
    line-height: 1;
  }
  .brand-band .brand-name { font-size: 38px; }
  .card-back .brand-name { font-size: 84px; letter-spacing: 0.09em; }
  .tagline {
    position: absolute;
    left: 416px;
    top: 56px;
    font-size: 23px;
    font-weight: 500;
    line-height: 28px;
    text-transform: uppercase;
    letter-spacing: 0.01em;
  }
  .person-name {
    position: absolute;
    left: 86px;
    top: 184px;
    font-size: 41px;
    font-weight: 500;
    line-height: 1;
  }
  .person-title {
    position: absolute;
    left: 88px;
    top: 238px;
    font-size: 25px;
    font-weight: 400;
    line-height: 1;
  }
  .contact {
    position: absolute;
    left: 88px;
    top: 296px;
    list-style: none;
    font-size: 26px;
    line-height: 33px;
    font-weight: 400;
  }
</style>
</head>
<body>
  <section class="card card-front">
    <div class="brand-band">
      <span class="brand-name">TIDEWELL</span>
    </div>
    <p class="tagline">Promotional merchandise<br>with a difference</p>
    <h1 class="person-name">Peter Hallorand</h1>
    <p class="person-title">Managing Director</p>
    <ul class="contact">
      <li>21 Kestrel Court Thornlea 4168</li>
      <li>mobile: 0438 612054</li>
      <li>email: tidewell@tidewellcoastal.com.au</li>
      <li>www.tidewell.com.au</li>
    </ul>
  </section>
  <section class="card card-back">
    <span class="brand-name">TIDEWELL</span>
  </section>
</body>
</html>
```